Car Spare Parts Packaging Box

I need a packaging design for car spare parts, specifically electrical parts or motor electric, such as fuel pump, motor power window, switch power window, motor fan radiator, sensor oxygen, starter, alternator, etc.

Our logo is as attached. Slogan "Premium Quality Auto Parts".
Font:
BinnerD (company name)
MictrogrammaDMedExt (slogan)

Color:
Blue - the gradients consist of C100 M100 Y0 K0 / C100 M0 Y0 K0
Yellow - gradients consist of C16 M32 Y100 K61 / C0 M0 Y100 K0

For reference:
KORVEL (multi products), Mirta (fuel pump, sensor oxygen), Votra (multi product)
Updates

Project Deadline Extended
Reason: Dear all, I still haven't find one suit my chemistry. Please browse existing worldwide brand from Japan and germany for more references. Since i am abroad at the moment, i will inform you more existing brand by tomorrow.

Project Deadline Extended
Reason: For some designers to finalize their work.

Industry/Entity Type

Electrical

Font styles to use
Serif
Sans Serif

Colors
0555a3
0892cd

Requirements
Must have
• 1. Space at one of the sides for label.
2. Gradient color design
3. Less white background.
Korvel n votra as main reference.
Nice to have
• wording: some of below options.
durable
reliable
high quality
best quality
quality guaranteed
replacement parts
long life
spare parts silhouette / blue print / real picture
Should not have
• 1. should not have car draw/picture, since we are selling car spare parts, not the car itself.
2. do not use common font: arial, times new roman.
Expect a new unique font.

```html
<!DOCTYPE html>
<html lang="en">
<head>
<meta charset="utf-8">
<title>Halvern Motor – Fuel Pump Box</title>
<link rel="stylesheet" href="https://fonts.googleapis.com/css2?family=Michroma&family=Roboto+Condensed:wght@400;700&display=swap">
<style>
  :root{
    --blue-deep:#1b1f8f;
    --blue-mid:#0555a3;
    --blue-bright:#0892cd;
    --gold-dark:#5e4a0a;
    --gold-bright:#c9b800;
    --yellow-text:#d8c400;
    --white:#ffffff;
    --ink-soft:#d9e6f5;
    --stage:#eef0f3;
    --pump-dark:#1c1c2c;
    --pump-mid:#3a3a52;
  }
  *{box-sizing:border-box;margin:0;padding:0}
  html,body{width:1200px;height:1000px;overflow:hidden}
  body{background:var(--stage);position:relative;font-family:"Michroma",sans-serif}

  .panel{
    position:absolute;width:400px;height:400px;overflow:hidden;
    background:linear-gradient(135deg,var(--blue-deep) 0%,var(--blue-mid) 45%,var(--blue-bright) 75%,var(--blue-mid) 100%);
  }
  .panel--top{left:600px;top:90px}
  .panel--side{left:200px;top:490px}
  .panel--front{left:600px;top:490px}

  .gold-band{
    position:absolute;top:0;width:40px;height:100%;
    background:linear-gradient(90deg,var(--gold-dark),var(--gold-bright) 55%,var(--gold-dark));
  }
  .panel--side .gold-band{right:0}
  .panel--front .gold-band{left:0}

  .brand-block{
    position:absolute;display:flex;flex-direction:column;align-items:center;
  }
  .brand{
    display:flex;align-items:center;gap:8px;
    color:var(--white);font-size:20px;letter-spacing:.3px;white-space:nowrap;
  }
  .brand__mark{width:16px;height:16px;background:var(--yellow-text)}
  .brand-tagline{
    margin-top:6px;font-size:8px;letter-spacing:2.6px;color:var(--ink-soft);white-space:nowrap;
    border-top:2px solid var(--yellow-text);padding-top:3px;
  }

  .pump-photo{
    position:absolute;border-radius:60px 20px 20px 60px;
    background:radial-gradient(ellipse at 40% 35%,var(--pump-mid) 0%,var(--pump-dark) 70%);
  }

  .product-name{position:absolute;color:var(--yellow-text);font-size:15px;white-space:nowrap}

  /* top panel */
  .panel--top .brand-block{left:20px;right:20px;top:26px}
  .panel--top .pump-photo{left:60px;top:110px;width:290px;height:150px;transform:rotate(-6deg)}
  .panel--top .product-name{left:140px;top:300px}

  /* front panel */
  .panel--front .brand-block{left:50px;right:10px;top:44px}
  .claims{
    position:absolute;left:80px;top:120px;color:var(--yellow-text);
    font-size:24px;line-height:34px;transform:rotate(-8deg);transform-origin:left top;
  }
  .panel--front .pump-photo{left:75px;top:228px;width:290px;height:108px;transform:rotate(-8deg)}
  .panel--front .product-name{left:170px;top:364px}

  /* side panel */
  .slogan{
    position:absolute;left:40px;top:40px;width:300px;text-align:center;
    color:var(--white);font-size:21px;line-height:32px;font-weight:400;
  }
  .company{
    position:absolute;left:40px;top:210px;width:150px;text-align:center;
    font-family:"Roboto Condensed",sans-serif;color:var(--white);font-size:10px;line-height:13px;
  }
  .contact{
    position:absolute;left:40px;top:300px;font-family:"Roboto Condensed",sans-serif;
    color:var(--white);font-size:15px;line-height:24px;
  }
  .cert-badges{position:absolute;left:210px;top:312px;display:flex;gap:8px}
  .cert-badge{width:22px;height:22px;border:2px solid var(--white);border-radius:3px}
  .cert-note{
    position:absolute;left:210px;top:342px;font-family:"Roboto Condensed",sans-serif;
    color:var(--ink-soft);font-size:9px;line-height:12px;
  }
</style>
</head>
<body>

  <section class="panel panel--top" aria-label="Top flap">
    <div class="brand-block">
      <div class="brand"><span>HALVERN</span><span class="brand__mark"></span><span>MOTOR</span></div>
      <div class="brand-tagline">PREMIUM QUALITY FUEL PUMPS</div>
    </div>
    <div class="pump-photo" role="img" aria-label="Photo of an electric fuel pump"></div>
    <div class="product-name">Fuel Pump</div>
  </section>

  <section class="panel panel--side" aria-label="Side panel">
    <h2 class="slogan">Premium Quality<br>Auto Parts</h2>
    <p class="company">Halvern Motor Parts Inc.<br>P.O. Box 4120<br>Ashford, Ohio<br>40217</p>
    <p class="contact">1 800 240-7788<br>www.halvernparts.com</p>
    <div class="cert-badges" aria-label="Certification marks">
      <span class="cert-badge"></span><span class="cert-badge"></span><span class="cert-badge"></span>
    </div>
    <p class="cert-note">ISO9001-2008<br>FUEL PUMP</p>
    <div class="gold-band"></div>
  </section>

  <section class="panel panel--front" aria-label="Front panel">
    <div class="gold-band"></div>
    <div class="brand-block">
      <div class="brand"><span>HALVERN</span><span class="brand__mark"></span><span>MOTOR</span></div>
      <div class="brand-tagline">PREMIUM QUALITY FUEL PUMPS</div>
    </div>
    <p class="claims">durable<br>reliable<br>long life</p>
    <div class="pump-photo" role="img" aria-label="Photo of an electric fuel pump with outlet nozzle"></div>
    <div class="product-name">Fuel Pump</div>
  </section>

</body>
</html>
```